Clinical Hypnotherapist needs business card design

I need a business card design that gives the impression of being approachable yet professional. As a clinical hypnotherapist I need to create trust from my clients to allow me access to their inner mind to enable them to make changes and to start to live the life that they want to live. My website is www.serenvale.com.au and I would like my business cards to reflect my website. I would like a space for appointment details on the back of the card.

```html
<!DOCTYPE html>
<html lang="en">
<head>
<meta charset="utf-8">
<title>Claire Hadley – Business Card</title>
<link href="https://fonts.googleapis.com/css2?family=EB+Garamond:wght@400&family=Open+Sans:wght@400;700&display=swap" rel="stylesheet">
<style>
  :root {
    --backdrop: #2b2b2b;
    --card: #ffffff;
    --plum: #8c1f80;
    --plum-deep: #6e1865;
  }
  * { margin: 0; padding: 0; box-sizing: border-box; }
  html, body {
    width: 1200px; height: 944px; overflow: hidden;
    background: var(--backdrop);
  }
  .canvas {
    position: relative; width: 1200px; height: 944px;
    display: flex; flex-direction: column; align-items: center; justify-content: center; gap: 42px;
  }
  .card {
    position: relative; width: 640px; height: 391px;
    background: var(--card);
    border-bottom: 8px solid var(--plum);
    color: var(--plum);
    overflow: hidden;
  }

  /* Front */
  .identity { position: absolute; left: 52px; top: 92px; }
  .identity__name {
    font-family: "EB Garamond", Georgia, serif;
    font-size: 62px; font-weight: 400; line-height: 1; letter-spacing: 0.5px;
  }
  .identity__role {
    font-family: "EB Garamond", Georgia, serif;
    font-size: 27px; line-height: 1.2; margin-top: 2px; margin-left: 28px;
  }
  .rule {
    position: absolute; left: 352px; right: 0; top: 190px;
    border-top: 1.5px solid var(--plum);
  }
  .contacts {
    position: absolute; left: 362px; top: 210px; list-style: none;
    font-family: "Open Sans", Arial, sans-serif; font-size: 14px; line-height: 24px;
  }
  .contacts li { display: flex; align-items: center; gap: 9px; }
  .contacts svg { width: 14px; height: 14px; fill: var(--plum); flex: none; }

  /* Back */
  .appointment { font-family: "Open Sans", Arial, sans-serif; padding: 40px 56px 0; }
  .appointment__title {
    text-align: center; font-size: 21px; font-weight: 700; letter-spacing: 0.5px;
  }
  .appointment__session {
    text-align: center; font-size: 19px; margin: 14px 0 6px;
  }
  .appointment__field {
    display: flex; align-items: flex-end; gap: 6px;
    font-size: 17px; height: 38px;
  }
  .appointment__field span:last-child {
    flex: 1; border-bottom: 2px dotted var(--plum); margin-bottom: 6px;
  }
</style>
</head>
<body>
<main class="canvas">
  <section class="card card--front" aria-label="Business card front">
    <div class="identity">
      <h1 class="identity__name">Claire Hadley</h1>
      <p class="identity__role">Clinical Hypnotherapist</p>
    </div>
    <div class="rule"></div>
    <ul class="contacts">
      <li>
        <svg viewBox="0 0 16 16" aria-hidden="true"><path d="M3 2h3l1.5 3.5-2 1.3a9 9 0 0 0 3.7 3.7l1.3-2L14 10v3a1 1 0 0 1-1 1A11 11 0 0 1 2 3a1 1 0 0 1 1-1z"/></svg>
        <span>0400 512 836</span>
      </li>
      <li>
        <svg viewBox="0 0 16 16" aria-hidden="true"><path d="M8 1a7 7 0 1 0 0 14A7 7 0 0 0 8 1zm0 1.5c.8 0 1.8 1.6 2.1 4.2H5.9C6.2 4.1 7.2 2.5 8 2.5zM2.6 8.2h2.9c.1 2.3.6 4 1.3 5.1A5.5 5.5 0 0 1 2.6 8.2zm0-1.5a5.5 5.5 0 0 1 4.2-4.5c-.7 1.1-1.2 2.8-1.3 4.5zm5.4 6.8c-.8 0-1.8-1.7-2-5.3h4c-.2 3.6-1.2 5.3-2 5.3zm1.2-.2c.7-1.1 1.2-2.8 1.3-5.1h2.9a5.5 5.5 0 0 1-4.2 5.1zm1.3-6.6c-.1-1.7-.6-3.4-1.3-4.5a5.5 5.5 0 0 1 4.2 4.5z"/></svg>
        <span>claire@serenvale.com.au</span>
      </li>
      <li>
        <svg viewBox="0 0 16 16" aria-hidden="true"><path d="M1 3.5h14v9H1zm1.5 1.2v.3L8 9l5.5-4v-.3zM2.5 6.6v4.7h11V6.6L8 10.6z"/></svg>
        <span>www.serenvale.com.au</span>
      </li>
    </ul>
  </section>

  <section class="card card--back appointment" aria-label="Business card back">
    <h2 class="appointment__title">APPOINTMENT</h2>
    <p class="appointment__session">Morning</p>
    <div class="appointment__field"><span>Date :</span><span></span></div>
    <div class="appointment__field"><span>Time :</span><span></span></div>
    <p class="appointment__session">Evening</p>
    <div class="appointment__field"><span>Date :</span><span></span></div>
    <div class="appointment__field"><span>Time :</span><span></span></div>
  </section>
</main>
</body>
</html>
```